Jewelry store needs fully functional Ecommerce website

Web Design Brief for our E-commerce Jewelry retail store.
Description

We need a fully coded Shopify website. The Shopify site will need to be fully functional with an Ecommerce integration (fully integrated with Paypal and All other gateways) and will need to be SEO optimized.
We sell jewelry items like: rings, earrings, necklaces etc. The website should have an elegant, modern, professional, fun, look.

***We would like the website to look and function similarly to this website:
https://velvorisco.com

Color Preference
Colors to be used are white background with black font and light pink/ purple/ gold tints. We have attached our logo as reference.

Functionalities
The store will function like a typical Ecommerce jewelry store, using the products/categories as the starting page. Going into individual product pages by selecting images and leading to a detailed “buy now” page for the selected product.

Target Market
Jewelry lovers.

Should Not Have:
- - Dull and common design
- - Messy/unstructured navigation

Coded - Design and coding required
Target Audience are women from 16-50 years old.
We will need to be able to add products and make modifications to the website as needed.

We need the following apps installed and Operating:
-Tally Shift; Order Look Up (rename “track your order”) ; Help Center (Questions and Answers) ; Pemmo Reviews; TXT Nudge; Drenoza Email Marketing ; Plivet (Facebook messenger bump) ; Vantro multi- currency (translate currency to buyer) ; Discounted Upsell ; Easy Contact form App
We will need all products imported: (below is information for importing products). We will provide all links that serve entire active item product catalog in shopifys import format:
DataFeed:

If you are getting started with Shopify, a combination of the Shopify Import Format and XML feeds is ideal. The Shopify Import Format will output a file that can be uploaded into Shopify’s product database. After you import, you can use the XML feed and a third party app to keep the inventory up to date in real time, take down items that go out of stock etc., all without regular human intervention. There a several Shopify apps that can do this type of feed integration. We have had a good experience with Tally Shift, which is an app that can be configured to accept our XML feed and update products on a set schedule. You can even set your own margins based on our wholesale price with this app.

Shopify Formatted HTML TableTo make it easier to get started on Shopify, we included a format that outputs the required fields for a product import in Shopify. In order to use the embedded Excel file, first open the file (Auto-Shopify-Datasheet-Format.xslx), Refresh it (under Data tab), and then Save As with a new file name in a CSV (UTF-8) file. That file can then be split into smaller CSV files (if there is a limit on the number of products per file) for import into Shopify.

Target Market(s)

Jewelry Lovers

Industry/Entity Type

Jewelry Store

Coding

Number of Pages Required

5+ page

Colors
eda3c7
d3a5cc
ffffff

Requirements
Must have
• Color Preference
Colors to be used are white background with black font and light pink/ purple/ gold tints.

https://velvorisco.com
Should not have
• Should Not Have:

```html
<!DOCTYPE html>
<html lang="en">
<head>
<meta charset="utf-8">
<title>Mara Velian Jewels — Gallery</title>
<link href="https://fonts.googleapis.com/css2?family=Montserrat:wght@300;400;500;600&family=Great+Vibes&display=swap" rel="stylesheet">
<style>
:root{
  --gold:#c9973f;
  --gold-soft:#e6cf9f;
  --ink:#2a2a2a;
  --muted:#777;
  --line:#e4e4e4;
  --band:#f6f6f6;
  --white:#fff;
  --dark:#2b2b2b;
}
*{box-sizing:border-box;margin:0;padding:0}
html,body{width:1200px;height:5319px;overflow:hidden}
body{font-family:'Montserrat',sans-serif;color:var(--ink);background:var(--white);position:relative}

/* header */
.site-header{position:relative;height:125px}
.brand{position:absolute;left:110px;top:52px;display:flex;align-items:center;gap:10px;font-size:17px;font-weight:500;color:var(--gold)}
.brand-dot{width:22px;height:22px;border-radius:50%;background:#d3a5cc}
.header-contact{position:absolute;top:52px;font-size:10px;color:var(--muted);line-height:1.4}
.header-contact strong{display:block;font-size:14px;font-weight:500;color:var(--ink)}
.header-contact.call{left:490px}
.header-contact.mail{left:650px}
.header-contact.mail strong{font-size:13px}
.btn-appoint{position:absolute;left:882px;top:50px;width:218px;height:42px;background:var(--gold);color:#fff;font-size:13px;font-weight:600;display:flex;align-items:center;justify-content:center}

.main-nav{position:absolute;left:97px;top:125px;width:1003px;height:45px;background:#fff;display:flex;align-items:center;z-index:2;font-size:13px}
.main-nav a{color:var(--ink);text-decoration:none;padding:0 36px;height:45px;display:flex;align-items:center;border-right:1px solid var(--line)}
.main-nav a.active{background:var(--gold);color:#fff;padding:0 34px}
.main-nav a:nth-child(5){border-right:0}
.caret{display:inline-block;margin-left:8px;border:4px solid transparent;border-top-color:var(--ink);transform:translateY(2px)}
.search{margin-left:auto;margin-right:8px;width:250px;height:32px;border:1px solid var(--line);display:flex;align-items:center;justify-content:space-between;padding:0 10px;font-size:10px;color:#aaa}

/* hero */
.hero{position:absolute;left:0;top:145px;width:1200px;height:300px;background:linear-gradient(90deg,#ececec 0%,#f0efee 35%,#e9e4dc 60%,#f3efe8 100%)}
.hero-photo{position:absolute;right:0;top:0;width:780px;height:300px;background:
  radial-gradient(ellipse 150px 90px at 66% 58%,#d9a873 0%,rgba(232,196,150,.7) 45%,rgba(240,230,215,0) 100%),
  radial-gradient(ellipse 260px 300px at 28% 50%,#fbf8f2 0%,#ece4d6 55%,rgba(236,228,214,0) 100%),
  linear-gradient(100deg,rgba(236,236,236,0) 0%,#efe8dc 40%,#f5efe5 100%)}
.hero-text{position:absolute;left:132px;top:100px}
.hero-text .script{font-family:'Great Vibes',cursive;font-size:38px;color:var(--gold)}
.hero-text h1{font-size:40px;font-weight:400;color:#333;margin-top:2px}
.side-tab{position:absolute;right:0;top:378px;width:42px;height:192px;background:var(--dark);color:var(--gold);z-index:3;display:flex;align-items:center;justify-content:center}
.side-tab span{transform:rotate(-90deg);white-space:nowrap;font-size:13px;font-weight:600;letter-spacing:1px}

/* gallery sections */
.gallery{position:absolute;left:0;width:1200px}
.gallery.band{background:var(--band)}
.gallery-head{position:absolute;left:97px;right:100px;top:70px;height:50px}
.gallery-head h2{font-size:37px;font-weight:400;color:#333}
.gallery-head h2::after{content:"";display:block;width:85px;height:3px;background:var(--gold);margin-top:10px}
.view-more{position:absolute;right:0;top:4px;width:148px;height:42px;background:var(--gold);color:#fff;font-size:13px;display:flex;align-items:center;justify-content:center;box-shadow:-6px -6px 0 -3px var(--gold-soft)}
.grid{position:absolute;left:97px;top:150px;width:1003px;display:grid;grid-template-columns:repeat(3,316px);column-gap:27px;row-gap:45px}
.card{position:relative;height:340px}
.card::before{content:"";position:absolute;left:0;right:0;top:25px;bottom:0;border:1px solid var(--gold-soft);border-top:0;background:#fff}
.card-photo{position:relative;margin-left:9px;width:299px;height:255px}
.card-name{position:relative;text-align:center;font-size:16px;color:#444;margin-top:22px}
.card-name::after{content:"";display:block;width:24px;height:2px;background:var(--gold);margin:12px auto 0}

/* photo tones: backdrop plus a soft glow in the piece's own colours */
.p-ring-filigree{background:radial-gradient(ellipse 110px 95px at 50% 48%,#e8b458 0%,#c48a3a 45%,rgba(196,138,58,0) 100%),radial-gradient(circle 40px at 52% 40%,rgba(150,110,190,.55),rgba(150,110,190,0)),linear-gradient(160deg,#6a4630,#b89a8c 70%,#e0c8bb)}
.p-ring-solitaire{background:radial-gradient(ellipse 70px 60px at 50% 55%,#f1f1f1 0%,#b8b8bc 40%,rgba(120,120,128,0) 100%),linear-gradient(180deg,#111 0%,#2b2b30 40%,#5e5e64 100%)}
.p-ring-leaf{background:radial-gradient(ellipse 50px 25px at 50% 52%,#c9a24e 0%,#a8862c 50%,rgba(200,150,120,0) 100%),linear-gradient(160deg,#a57763,#dcb3a0 55%,#efd4c6)}
.p-ring-band{background:radial-gradient(ellipse 55px 110px at 45% 45%,#d9dce8 0%,#6c7184 45%,rgba(40,40,52,0) 100%),linear-gradient(180deg,#14141c 0%,#262633 60%,#c9ad98 100%)}
.p-ring-ruby{background:radial-gradient(ellipse 50px 45px at 48% 40%,#a3175a 0%,#c84d8a 45%,rgba(220,226,238,0) 100%),linear-gradient(160deg,#b9c4d6,#eef1f6 55%,#d9c6b8)}
.p-ring-script{background:radial-gradient(ellipse 130px 45px at 50% 55%,#3b2416 0%,#6e4a36 55%,rgba(160,120,100,0) 100%),linear-gradient(180deg,#2a1a12 0%,#a8806a 45%,#c9a790 100%)}
.p-bridal-tiara{background:radial-gradient(ellipse 80px 120px at 30% 55%,#e9d3c5 0%,#c79e86 50%,rgba(60,40,35,0) 100%),linear-gradient(90deg,#3b2a24 0%,#d4c2b4 60%,#efe6dd 100%)}
.p-bridal-butterfly{background:radial-gradient(ellipse 40px 35px at 55% 52%,#efe6ec 0%,#d9c3d1 50%,rgba(160,120,110,0) 100%),linear-gradient(180deg,#a78670 0%,#c7ada6 50%,#e3d0da 100%)}
.p-bridal-crown{background:radial-gradient(ellipse 110px 50px at 50% 15%,#eceef2 0%,#c2c4ca 50%,rgba(200,170,150,0) 100%),radial-gradient(ellipse 90px 110px at 50% 65%,#f0d1bd 0%,#d6a98e 50%,rgba(150,110,90,0) 100%),linear-gradient(160deg,#a78a74,#8f6f5c)}
.p-bridal-necklace{background:radial-gradient(ellipse 60px 45px at 50% 65%,#3f7d52 0%,#9b2a3a 45%,rgba(168,128,106,0) 100%),linear-gradient(160deg,#8e6a56,#b28c76 60%,#c9a790)}
.p-bridal-set{background:radial-gradient(circle 28px at 30% 62%,#8d1530 0%,rgba(141,21,48,0) 100%),radial-gradient(circle 22px at 75% 40%,#8d1530 0%,rgba(141,21,48,0) 100%),linear-gradient(180deg,#1b1b1d 0%,#3a3a40 45%,#e6e6ea 100%)}
.p-bridal-curls{background:radial-gradient(ellipse 70px 90px at 52% 50%,#f1d4c2 0%,#d2a688 50%,rgba(120,80,50,0) 100%),linear-gradient(160deg,#6e4a2c,#b98c62 50%,#ece1d6)}
.p-color-topaz{background:radial-gradient(ellipse 55px 50px at 55% 52%,#2fc4c9 0%,#3ca6ae 45%,rgba(230,190,165,0) 100%),linear-gradient(140deg,#4e9bb3 0%,#e4bea6 50%,#f3d9c7 100%)}
.p-color-cluster{background:radial-gradient(ellipse 55px 60px at 50% 40%,#6a0f35 0%,#a52a5c 40%,rgba(220,220,226,0) 100%),linear-gradient(180deg,#f7f7f8,#e4e4e8 60%,#cfcfd5)}
.p-color-ruby-necklace{background:radial-gradient(ellipse 130px 50px at 50% 68%,#c0102f 0%,#d83a55 45%,rgba(245,232,228,0) 100%),radial-gradient(ellipse 60px 18px at 48% 8%,#c8152f,rgba(200,21,47,0)),linear-gradient(180deg,#f6ebe6,#f4e6e2)}
.p-color-model{background:radial-gradient(ellipse 75px 60px at 45% 82%,#c99a4c 0%,#b48863 45%,rgba(200,170,150,0) 100%),radial-gradient(ellipse 85px 110px at 40% 35%,#e8c9b8 0%,#cda48f 55%,rgba(120,90,80,0) 100%),linear-gradient(160deg,#8e7468,#d8cbc3)}
.p-color-pendant{background:radial-gradient(circle 38px at 50% 55%,#8e1d38 0%,#b54a5e 50%,rgba(210,190,190,0) 100%),linear-gradient(180deg,#c4a89a,#e1d1cf 60%,#ecdfe3)}
.p-color-hoops{background:radial-gradient(ellipse 90px 75px at 48% 48%,#c4285a 0%,#b9a4b6 45%,rgba(230,220,212,0) 100%),linear-gradient(180deg,#d8c6b6,#f2ece7 55%,#e0d3ca)}
.p-gold-bangles{background:radial-gradient(ellipse 140px 90px at 50% 50%,#f0c869 0%,#c3892f 45%,rgba(70,40,20,0) 100%),linear-gradient(180deg,#3a2414,#6b4520)}
.p-gold-necklace{background:radial-gradient(ellipse 80px 55px at 45% 78%,#d7a24e 0%,#a86c34 45%,rgba(60,30,20,0) 100%),radial-gradient(ellipse 70px 80px at 50% 25%,#c08b6e 0%,rgba(120,70,50,0) 100%),linear-gradient(160deg,#2a1810,#5a3826)}
.p-gold-pearl{background:radial-gradient(circle 38px at 35% 48%,#fbfaf6 0%,#e8e2d6 60%,rgba(240,240,240,0) 100%),radial-gradient(ellipse 90px 55px at 62% 58%,#e0aa5a 0%,#c98d3c 45%,rgba(230,230,232,0) 100%),linear-gradient(180deg,#e9e9ec,#fbfbfb)}
.p-gold-earrings{background:radial-gradient(ellipse 70px 65px at 55% 80%,#d8a457 0%,#c9a56a 45%,rgba(200,170,170,0) 100%),radial-gradient(ellipse 80px 100px at 50% 35%,#ecccc0 0%,#d4aaa0 55%,rgba(140,110,120,0) 100%),linear-gradient(160deg,#8d7580,#d4c4c6)}
.p-gold-drops{background:radial-gradient(ellipse 30px 70px at 30% 65%,#d9a24c 0%,rgba(217,162,76,0) 100%),radial-gradient(ellipse 70px 95px at 55% 40%,#d9ad95 0%,#a8745d 55%,rgba(50,30,25,0) 100%),linear-gradient(160deg,#2c1c16,#5c3e32)}
.p-gold-bow{background:radial-gradient(ellipse 70px 55px at 50% 62%,#f1d9a0 0%,#d3a25d 45%,rgba(190,140,100,0) 100%),linear-gradient(170deg,#b07a4e,#d9a98a 55%,#c89272)}

/* contact */
.contact-box{position:absolute;left:97px;top:4340px;width:1003px;height:520px;background:#fff;box-shadow:0 0 14px rgba(0,0,0,.08)}
.contact-box h2{position:absolute;left:38px;top:60px;font-size:37px;font-weight:400;line-height:1.3;color:#333}
.contact-box h2::after,.info h3::after{content:"";display:block;width:85px;height:3px;background:var(--gold);margin-top:10px}
.form{position:absolute;left:38px;top:205px;width:500px;display:grid;grid-template-columns:1fr 1fr;gap:18px 20px}
.field{height:38px;border:1px solid var(--line);font-size:10px;color:#aaa;padding:12px 12px}
.field.wide{grid-column:1/3;height:84px}
.send{grid-column:1;width:172px;height:44px;border:1px solid var(--gold);color:var(--gold);font-size:12px;display:flex;align-items:center;justify-content:center;margin-top:8px}
.info{position:absolute;left:676px;top:55px;width:300px}
.info h3{font-size:30px;font-weight:400;line-height:1.3;color:#333}
.info dl{margin-top:22px;font-size:13px}
.info dt{font-weight:600}
.info dd{font-size:11px;color:#555;margin:4px 0 14px;line-height:1.3}
.info h4{font-size:24px;font-weight:400;line-height:1.35;color:#333;margin-top:22px}
.info h4::after{content:"";display:block;width:85px;height:3px;background:var(--gold);margin-top:8px}
.call-btn{display:flex;align-items:center;gap:12px;margin-top:26px;width:208px;height:48px;background:var(--gold);color:#fff;font-size:18px;padding-left:22px}

/* footer */
.site-footer{position:absolute;left:0;top:4930px;width:1200px;height:389px;background:var(--band)}
.foot-brand{position:absolute;left:110px;top:70px;display:flex;align-items:center;gap:10px;font-size:17px;font-weight:500;color:var(--gold)}
.foot-about{position:absolute;left:97px;top:140px;width:318px;font-size:11px;line-height:1.75;color:#555}
.socials{position:absolute;left:97px;top:283px;display:flex;gap:12px}
.socials span{width:28px;height:28px;border-radius:50%;background:var(--gold)}
.foot-col{position:absolute;top:95px;font-size:11px;color:#555}
.foot-col h5{font-size:15px;font-weight:600;color:#333;margin-bottom:10px}
.foot-col h5::after{content:"";display:block;width:40px;height:2px;background:var(--gold);margin-top:8px}
.foot-col li{list-style:none;line-height:30px}
.foot-col p{line-height:1.5}
.foot-col b{font-size:13px;font-weight:600;color:#333;display:block;margin-top:2px}
.copyright{position:absolute;left:0;right:0;bottom:12px;text-align:center;font-size:12px;color:#444}
</style>
</head>
<body>

<header class="site-header">
  <div class="brand"><span class="brand-dot"></span>Mara Velian</div>
  <div class="header-contact call">Call us for any Query<strong>+420 555 0190</strong></div>
  <div class="header-contact mail">Email us for any info<strong>info@maravelianjewels.com</strong></div>
  <div class="btn-appoint">Set up an Appointment</div>
</header>

<section class="hero">
  <div class="hero-photo" role="img" aria-label="Strands of pearls with a pair of gold wedding rings"></div>
  <div class="hero-text">
    <div class="script">Mara Velian Jewels</div>
    <h1>Gallery</h1>
  </div>
</section>

<nav class="main-nav">
  <a class="active">Home</a>
  <a>About us</a>
  <a>Jewelry<span class="caret"></span></a>
  <a>Our Story</a>
  <a>Contact us</a>
  <div class="search">Search Jewelry
    <svg width="12" height="12" viewBox="0 0 12 12"><circle cx="5" cy="5" r="3.6" fill="none" stroke="#555" stroke-width="1.2"/><line x1="7.6" y1="7.6" x2="11" y2="11" stroke="#555" stroke-width="1.2"/></svg>
  </div>
</nav>

<div class="side-tab"><span>CONTACT US &nbsp;‹</span></div>

<section class="gallery" style="top:445px;height:975px">
  <div class="gallery-head"><h2>Engagement Rings</h2><div class="view-more">View More</div></div>
  <div class="grid">
    <div class="card"><div class="card-photo p-ring-filigree" role="img" aria-label="Gold filigree ring with coloured stones"></div><p class="card-name">Ring Item-01</p></div>
    <div class="card"><div class="card-photo p-ring-solitaire" role="img" aria-label="Solitaire diamond ring in a box"></div><p class="card-name">Ring Item-02</p></div>
    <div class="card"><div class="card-photo p-ring-leaf" role="img" aria-label="Gold leaf ring worn on a hand"></div><p class="card-name">Ring Item-03</p></div>
    <div class="card"><div class="card-photo p-ring-band" role="img" aria-label="Diamond band ring on a display cone"></div><p class="card-name">Ring Item-04</p></div>
    <div class="card"><div class="card-photo p-ring-ruby" role="img" aria-label="Ruby halo ring"></div><p class="card-name">Ring Item-05</p></div>
    <div class="card"><div class="card-photo p-ring-script" role="img" aria-label="Script love ring on a suede display"></div><p class="card-name">Ring Item-06</p></div>
  </div>
</section>

<section class="gallery band" style="top:1420px;height:975px">
  <div class="gallery-head"><h2>Bridal Jewelry</h2><div class="view-more">View More</div></div>
  <div class="grid">
    <div class="card"><div class="card-photo p-bridal-tiara" role="img" aria-label="Bride wearing a tiara and earrings"></div><p class="card-name">Bridal Item-01</p></div>
    <div class="card"><div class="card-photo p-bridal-butterfly" role="img" aria-label="Butterfly pendant necklace on a display"></div><p class="card-name">Bridal Item-02</p></div>
    <div class="card"><div class="card-photo p-bridal-crown" role="img" aria-label="Bride wearing a crown and drop earrings"></div><p class="card-name">Bridal Item-03</p></div>
    <div class="card"><div class="card-photo p-bridal-necklace" role="img" aria-label="Gold necklace with emeralds and rubies"></div><p class="card-name">Bridal Item-04</p></div>
    <div class="card"><div class="card-photo p-bridal-set" role="img" aria-label="Ruby pendant and ring set in boxes"></div><p class="card-name">Bridal Item-05</p></div>
    <div class="card"><div class="card-photo p-bridal-curls" role="img" aria-label="Bride with curls and a tiara"></div><p class="card-name">Bridal Item-06</p></div>
  </div>
</section>

<section class="gallery" style="top:2395px;height:957px">
  <div class="gallery-head"><h2>Colored Stones Jewelry</h2><div class="view-more">View More</div></div>
  <div class="grid">
    <div class="card"><div class="card-photo p-color-topaz" role="img" aria-label="Blue topaz ring on a hand"></div><p class="card-name">Colored Item-01</p></div>
    <div class="card"><div class="card-photo p-color-cluster" role="img" aria-label="Ruby and diamond cluster ring"></div><p class="card-name">Colored Item-02</p></div>
    <div class="card"><div class="card-photo p-color-ruby-necklace" role="img" aria-label="Ruby statement necklace"></div><p class="card-name">Colored Item-03</p></div>
    <div class="card"><div class="card-photo p-color-model" role="img" aria-label="Model wearing a coloured stone necklace"></div><p class="card-name">Colored Item-04</p></div>
    <div class="card"><div class="card-photo p-color-pendant" role="img" aria-label="Red stone pendant necklace"></div><p class="card-name">Colored Item-05</p></div>
    <div class="card"><div class="card-photo p-color-hoops" role="img" aria-label="Ruby and diamond hoop earrings"></div><p class="card-name">Colored Item-06</p></div>
  </div>
</section>

<section class="gallery band" style="top:3352px;height:988px">
  <div class="gallery-head"><h2>18 Karat Italian Gold</h2><div class="view-more">View More</div></div>
  <div class="grid">
    <div class="card"><div class="card-photo p-gold-bangles" role="img" aria-label="Stacked gold bangles"></div><p class="card-name">Colored Item-01</p></div>
    <div class="card"><div class="card-photo p-gold-necklace" role="img" aria-label="Model wearing a gold necklace"></div><p class="card-name">Colored Item-02</p></div>
    <div class="card"><div class="card-photo p-gold-pearl" role="img" aria-label="Gold pearl and diamond rings"></div><p class="card-name">Colored Item-03</p></div>
    <div class="card"><div class="card-photo p-gold-earrings" role="img" aria-label="Model wearing gold earrings and ring"></div><p class="card-name">Colored Item-04</p></div>
    <div class="card"><div class="card-photo p-gold-drops" role="img" aria-label="Model wearing gold drop earrings"></div><p class="card-name">Colored Item-05</p></div>
    <div class="card"><div class="card-photo p-gold-bow" role="img" aria-label="Gold bow pendant necklace"></div><p class="card-name">Colored Item-06</p></div>
  </div>
</section>

<section class="contact-box">
  <h2>Contact Mara<br>Velian Jewels</h2>
  <form class="form">
    <div class="field">First Name</div>
    <div class="field">Last Name</div>
    <div class="field">Email</div>
    <div class="field">Phone Number</div>
    <div class="field wide">Message</div>
    <div class="send">Send Message</div>
  </form>
  <div class="info">
    <h3>Contact<br>Information</h3>
    <dl>
      <dt>Phone:</dt><dd>555.0142.77</dd>
      <dt>Address:</dt><dd>Lorem ipsum 123 city abc<br>ipsum dolor site mit</dd>
    </dl>
    <h4>Quick Information<br>Mara Velian Jewels</h4>
    <div class="call-btn">
      <svg width="16" height="16" viewBox="0 0 24 24"><path fill="#fff" d="M6.6 10.8a15.1 15.1 0 0 0 6.6 6.6l2.2-2.2a1 1 0 0 1 1-.25 11.4 11.4 0 0 0 3.6.57 1 1 0 0 1 1 1V20a1 1 0 0 1-1 1A17 17 0 0 1 3 4a1 1 0 0 1 1-1h3.5a1 1 0 0 1 1 1c0 1.25.2 2.45.57 3.57a1 1 0 0 1-.25 1z"/></svg>
      555.0142.77
    </div>
  </div>
</section>

<footer class="site-footer">
  <div class="foot-brand"><span class="brand-dot"></span>Mara Velian</div>
  <p class="foot-about">Mara Velian is a jewelry designer based in Lebanon. She grew up around jewelry in a family business that has been in the market for decades, making gold and precious stones a natural and essential part of her life.</p>
  <div class="socials"><span></span><span></span><span></span><span></span></div>
  <div class="foot-col" style="left:502px"><h5>Useful Links</h5><ul><li>Home</li><li>About us</li><li>Jewelry</li><li>Our Story</li><li>Contact us</li></ul></div>
  <div class="foot-col" style="left:697px"><h5>Quick Links</h5><ul><li>Engagement rings</li><li>Bridal Jewelry</li><li>Precious stones Jewelry</li><li>18 Karat Italian Gold</li><li>Privacy policy</li></ul></div>
  <div class="foot-col" style="left:937px"><h5>Contact Us</h5><p><b>Phone:</b>555.0142.77</p><p style="margin-top:26px"><b>Address:</b>Lorem ipsum 123 city abc<br>ipsum dolor site mit</p></div>
  <p class="copyright">© 2018 Mara Velian Jewels. All rights reserved.</p>
</footer>

</body>
</html>
```